Workers comp/Business Ins/ Payroll- Postcard

I own an insurance agency.  I'm interested in getting some professional advice on how to design a message for what i want to sell.  The products I want to sell are 1) Workers compensation 2) business Insurance 3) Payroll processing. They are integrated together but I'm not sure if it's too much to put on a postcard and if I don't put it on a postcard I could be missing out on sales.
I have the ability to look up what Insurance company a business has their workers compensation  policy with, along with their expiration date.  Based on that information I can tell if the business is overpaying for their Workers compensation. insurance. Most companies are overpaying so I can usually save a company money very quickly if I can get in front of them. Some businesses work with a broker such as myself and buy a policy. When it's done this way, the business ESTIMATES his payroll for the year and at the end of the year they have to complete an audit to find out the actual payroll. Based on audit, they will either owe more money if they were low or get money back if they were high. The other way a business buys a workers comp. policy is with their payroll company. The payroll company will place the policy on Pay -as- you -go which means when you pay your employees every week they  will also calculate how much the workers comp premium is for the week and take that amount out of their checking account. This method avoids large down payments, helps with cash flow and should be very accurate at the end of the policy term.  This is by far the best way to do this for the businessowner. My company also has payroll company and we do this for the insured as well. However, most payroll company's such as QRT and Wagelon charge the customer $15 every time they do this so if it's weekly it is another $780 a year.  We also complete the insured's audit for them which is a big headache for the businessowner.
One of our biggest benefits of doing business with our company is we have a  Steady Rate Forever. When you sign up your base price will never increase. Payroll companies are famous for "discounting a new client" only to increase the rate in a few months later. Our service is also superior to the other payroll companies who use overseas service centers. We have staff within our office and we can answer questions quickly. We usually save businesses money on  their Payroll processing but it's not what we focus on- We focus on the Service.
Business Insurance- One of our main companies that we represent is Brindle Insurance. Brindle is very competitive and we usually write business accounts where we save the business owner money but offer superior coverages.
in summary, I'm offering 1) better workers compensation rates 2) Pay as you go workers comp. 3) Steady Rate, audits done for you, and superior customer service with our payroll company 4) savings on their business insurance with superior coverages.
Sometimes when we talk to an insured we may start with just their payroll and later get the WC and business liability. Each account is different and we do not pressure people to make decisions and we do what is right for them.  The biggest takeaway is we take some things off the plate for the businessowner where they can make just one phone call to get what they need done.  Our Website is www.harbor-mutual.example. my email is tomk@harbor-mutual.example if you have any questions.
Thank You
Tom Kessor

Target Market(s)
Small business owners 1-50 employees
Industry/Entity Type
Insurance and Payroll
Font styles to use
Other font styles liked:
- Let designer choose

Colors
Designer to choose colors to be used in the design.
Requirements
Must have
- It shouldn't be boring- needs to stand out- can use 6x11 inch postcard

Nice to have
- I like humor but not a must

Should not have
- Nothing I can think of

```html
<!DOCTYPE html>
<html lang="en">
<head>
<meta charset="utf-8">
<title>Harbor Mutual Insurance – Postcard</title>
<link rel="stylesheet" href="https://fonts.googleapis.com/css2?family=Playfair+Display:wght@400;700&family=Roboto:ital,wght@0,400;0,700;1,700&display=swap">
<style>
  :root {
    --brand-red: #7a2b30;
    --brand-grey: #8c8c8c;
    --soft-grey: #e6e6e6;
    --page-bg: #e9e9e9;
    --ink: #1e1e1e;
    --white: #ffffff;
    --serif: "Playfair Display", Georgia, serif;
    --sans: "Roboto", Arial, sans-serif;
  }
  * { box-sizing: border-box; margin: 0; padding: 0; }
  html, body { width: 1009px; height: 1200px; overflow: hidden; background: var(--page-bg); }
  .stage { position: absolute; left: 0; top: 0; width: 980px; height: 1166px; transform: scale(1.0296, 1.0292); transform-origin: 0 0; }
  .card { position: absolute; left: 43px; width: 885px; background: var(--white); overflow: hidden; box-shadow: 0 2px 6px rgba(0,0,0,.18); font-family: var(--sans); }
  .card--front { top: 72px; height: 486px; }
  .card--back { top: 603px; height: 484px; }
  .card svg.shapes { position: absolute; inset: 0; }
  .abs { position: absolute; }

  .brand { text-align: center; color: var(--brand-red); font-family: var(--serif); font-weight: 400; line-height: 1; }
  .brand__name { font-size: 29px; letter-spacing: .5px; }
  .brand__sub { font-size: 11px; letter-spacing: 7px; margin-top: 5px; }

  .intro { left: 27px; top: 133px; width: 310px; font-size: 10.6px; line-height: 14.6px; color: var(--ink); }
  .intro b { font-weight: 700; }

  .headline { left: 487px; top: 34px; width: 375px; text-align: center; font-family: var(--serif); }
  .headline__main { font-size: 40px; line-height: 44px; color: var(--brand-grey); letter-spacing: .3px; }
  .headline__main span { color: var(--brand-red); }
  .headline__sub { font-size: 18.5px; color: var(--brand-grey); letter-spacing: .6px; line-height: 22px; }
  .lines-banner { left: 487px; top: 108px; width: 375px; height: 32px; background: var(--brand-red); border: 2px solid var(--white); outline: 1px solid var(--brand-red); color: var(--white); font-family: var(--serif); font-size: 19.5px; text-align: center; line-height: 27px; }

  .benefits { left: 33px; top: 274px; list-style: none; }
  .benefits li { display: flex; align-items: center; height: 26.8px; color: var(--white); font-size: 12.2px; letter-spacing: .2px; }
  .benefits svg { width: 15px; height: 15px; margin-right: 11px; flex: none; }

  .address { left: 548px; top: 402px; font-size: 10.6px; line-height: 16px; font-weight: 700; color: var(--ink); }
  .address span { color: var(--brand-red); }

  .contact { display: flex; align-items: center; color: var(--white); font-size: 12px; letter-spacing: .2px; }
  .contact svg { width: 14px; height: 14px; margin-right: 9px; }
  .website { color: var(--white); font-family: var(--serif); font-weight: 700; font-size: 17px; letter-spacing: .6px; text-align: center; }

  .service-tab { color: var(--white); font-family: var(--serif); font-size: 15px; letter-spacing: .4px; left: 22px; }
  .rating { left: 88px; top: 215px; color: var(--white); font-size: 21px; letter-spacing: 4px; }
  .testimonial { left: 34px; top: 248px; width: 250px; color: var(--white); font-style: italic; font-weight: 700; font-size: 10.6px; line-height: 14.5px; white-space: nowrap; }
  .mission { left: 318px; top: 115px; width: 236px; text-align: right; font-size: 10.8px; line-height: 15.2px; color: var(--ink); }
  .mission b { font-weight: 700; }
  .mission .mission__label { color: var(--brand-red); }
</style>
</head>
<body>
<div class="stage">

  <section class="card card--front">
    <svg class="shapes" width="885" height="486" viewBox="0 0 885 486">
      <defs>
        <linearGradient id="deskGlow" x1="0" y1="0" x2="1" y2="1">
          <stop offset="0" stop-color="#d9c7a8"/>
          <stop offset=".45" stop-color="#b9c6d6"/>
          <stop offset="1" stop-color="#e9eef3"/>
        </linearGradient>
      </defs>
      <polygon points="497,0 885,0 885,393 497,393 347,250 257,250" fill="var(--soft-grey)"/>
      <polygon role="img" aria-label="Photo: an advisor's hand signing insurance paperwork with charts at a desk" points="427,123 885,123 885,393 497,393 347,255" fill="url(#deskGlow)"/>
      <polygon points="0,250 347,250 537,438 0,438" fill="var(--brand-red)"/>
      <rect x="0" y="443" width="885" height="43" fill="var(--brand-grey)"/>
      <polygon points="540,443 885,443 885,486 572,486" fill="var(--brand-red)"/>
      <circle cx="510" cy="416" r="14" fill="var(--brand-grey)"/>
      <path d="M510 407a5.5 5.5 0 0 0-5.5 5.5c0 4 5.5 10 5.5 10s5.5-6 5.5-10a5.5 5.5 0 0 0-5.5-5.5zm0 7.6a2.1 2.1 0 1 1 0-4.2 2.1 2.1 0 0 1 0 4.2z" fill="var(--white)"/>
    </svg>

    <div class="brand abs" style="left:64px; top:72px; width:250px;">
      <div class="brand__name">HARBOR MUTUAL</div>
      <div class="brand__sub">INSURANCE</div>
    </div>

    <p class="intro abs"><b>Founded in 1993</b>, Harbor Mutual of Western New York has provided thousands of individuals, families &amp; businesses in the greater Rochester area with customized, comprehensive insurance solutions within their budgets.<br>Every customer received personalized consultation, dedicated attention, and has access to our many world-class insurance carriers.</p>

    <div class="headline abs">
      <div class="headline__main"><span>TRUSTED</span> ADVISOR</div>
      <div class="headline__sub">FOR ALL OF YOUR INSURANCE NEEDS</div>
    </div>
    <div class="lines-banner abs">AUTO • HOME • BUSINESS • PAYROLL</div>

    <ul class="benefits abs">
      <li><svg viewBox="0 0 15 15"><rect x="1" y="3" width="11" height="11" fill="none" stroke="#fff" stroke-width="1.6"/><path d="M3.5 8l3 3 7-9" fill="none" stroke="#fff" stroke-width="2"/></svg>BETTER WORKERS COMPENSATION RATES</li>
      <li><svg viewBox="0 0 15 15"><rect x="1" y="3" width="11" height="11" fill="none" stroke="#fff" stroke-width="1.6"/><path d="M3.5 8l3 3 7-9" fill="none" stroke="#fff" stroke-width="2"/></svg>PAY AS YOU GO WORKERS COMPENSATION</li>
      <li><svg viewBox="0 0 15 15"><rect x="1" y="3" width="11" height="11" fill="none" stroke="#fff" stroke-width="1.6"/><path d="M3.5 8l3 3 7-9" fill="none" stroke="#fff" stroke-width="2"/></svg>STEADY RATE</li>
      <li><svg viewBox="0 0 15 15"><rect x="1" y="3" width="11" height="11" fill="none" stroke="#fff" stroke-width="1.6"/><path d="M3.5 8l3 3 7-9" fill="none" stroke="#fff" stroke-width="2"/></svg>AUDITS DONE FOR YOU</li>
      <li><svg viewBox="0 0 15 15"><rect x="1" y="3" width="11" height="11" fill="none" stroke="#fff" stroke-width="1.6"/><path d="M3.5 8l3 3 7-9" fill="none" stroke="#fff" stroke-width="2"/></svg>SUPERIOR CUSTOMER SERVICE</li>
      <li><svg viewBox="0 0 15 15"><rect x="1" y="3" width="11" height="11" fill="none" stroke="#fff" stroke-width="1.6"/><path d="M3.5 8l3 3 7-9" fill="none" stroke="#fff" stroke-width="2"/></svg>SAVINGS ON BUSINESS INSURANCE WITH SUPERIOR COVERAGES</li>
    </ul>

    <div class="address abs">
      1200 LINDEN ROAD | MAPLEWOOD, NY 14000 | <span>555-310-4420</span><br>
      42 ELM PLACE | CEDARVIEW, NY 14001 | <span>555-310-4471</span>
    </div>

    <div class="contact abs" style="left:33px; top:454px;">
      <svg viewBox="0 0 14 14"><circle cx="7" cy="7" r="7" fill="var(--brand-red)"/><path d="M4.6 3.6l1.3-.3.8 1.9-.9.7a5 5 0 0 0 2.3 2.3l.7-.9 1.9.8-.3 1.3c-3 .3-6.1-2.8-5.8-5.8z" fill="#fff"/></svg>
      555.310.4420 OR (800) 555-0147
    </div>
    <div class="contact abs" style="left:258px; top:454px;">
      <svg viewBox="0 0 14 14"><circle cx="7" cy="7" r="7" fill="var(--brand-red)"/><rect x="3.5" y="4.5" width="7" height="5" fill="#fff"/><path d="M3.5 4.5L7 7.3l3.5-2.8" fill="none" stroke="var(--brand-red)" stroke-width=".9"/></svg>
      TOMK@HARBOR-MUTUAL.EXAMPLE
    </div>
    <div class="website abs" style="left:560px; top:452px; width:325px;">WWW.HARBOR-MUTUAL.EXAMPLE</div>
  </section>

  <section class="card card--back">
    <svg class="shapes" width="885" height="484" viewBox="0 0 885 484">
      <defs>
        <linearGradient id="streetTone" x1="0" y1="0" x2="0" y2="1">
          <stop offset="0" stop-color="#bdbdbd"/>
          <stop offset=".7" stop-color="#8d8d8d"/>
          <stop offset="1" stop-color="#cfcfcf"/>
        </linearGradient>
      </defs>
      <polygon points="0,0 67,0 360,290 360,447 0,447" fill="var(--brand-red)"/>
      <polygon points="0,69 205,69 227,102 0,102" fill="var(--brand-grey)"/>
      <polygon points="0,117 250,117 272,149 0,149" fill="var(--brand-grey)"/>
      <polygon points="0,164 295,164 317,197 0,197" fill="var(--brand-grey)"/>
      <polygon role="img" aria-label="Photo: the agency's two-storey brick office building on a street corner" points="0,330 40,318 130,322 300,292 340,276 440,274 562,300 562,447 0,447" fill="url(#streetTone)"/>
      <rect x="0" y="447" width="560" height="37" fill="var(--brand-grey)"/>
      <polygon points="528,447 885,447 885,484 548,484" fill="var(--brand-red)"/>
    </svg>

    <div class="service-tab abs" style="top:76px;">PAYROLL PROCESSING</div>
    <div class="service-tab abs" style="top:123px;">BUSINESS INSURANCE</div>
    <div class="service-tab abs" style="top:170px;">WORKERS COMPENSATION</div>

    <div class="rating abs">★★★★★</div>
    <p class="testimonial abs">Harbor Mutual has been a joy to work with.<br>I'd recommend them to anyone who needs help<br>with their insurance. - Dan R., New York</p>

    <div class="brand abs" style="left:299px; top:56px; width:250px;">
      <div class="brand__name">HARBOR MUTUAL</div>
      <div class="brand__sub">INSURANCE</div>
    </div>

    <p class="mission abs"><b><span class="mission__label">OUR MISSION</span> is to be your most</b><br><b>Trusted Advisor</b> for all of your insurance needs, from home and auto plans to life insurance, to the specialty protections required for your business. We are consultative and develop an insurance program specific to your needs, providing just the right amount of protection suitable for your assets, goals and situation.</p>

    <div class="contact abs" style="left:60px; top:457px;">
      <svg viewBox="0 0 14 14"><circle cx="7" cy="7" r="7" fill="var(--brand-red)"/><path d="M4.6 3.6l1.3-.3.8 1.9-.9.7a5 5 0 0 0 2.3 2.3l.7-.9 1.9.8-.3 1.3c-3 .3-6.1-2.8-5.8-5.8z" fill="#fff"/></svg>
      555.310.4420 OR (800) 555-0147
    </div>
    <div class="contact abs" style="left:285px; top:457px;">
      <svg viewBox="0 0 14 14"><circle cx="7" cy="7" r="7" fill="var(--brand-red)"/><rect x="3.5" y="4.5" width="7" height="5" fill="#fff"/><path d="M3.5 4.5L7 7.3l3.5-2.8" fill="none" stroke="var(--brand-red)" stroke-width=".9"/></svg>
      TOMK@HARBOR-MUTUAL.EXAMPLE
    </div>
    <div class="website abs" style="left:555px; top:455px; width:330px;">WWW.HARBOR-MUTUAL.EXAMPLE</div>
  </section>

</div>
</body>
</html>
```